Harbor Crest Exteriors Inc Business cards

Commercial and Residential Roofing contractor needs design logo and card design. Can be single or double sided but must incorporate:
Persons Name:
Persons Title:
Mailing Address: PO Box 3716
Physical Address: 41 Birch Lane
Linwood, Me. 01623
800-615-2284
508-762-2284
Fax: 508-762-2231
Cell: Person Cell number
email address
Website: WWW.harborcrestexteriors.example

Target Market(s)

Residential home owners and commercial building owners

Industry/Entity Type

Roofing

Contact Information for Business Card

Persons Name:
Persons Title:
Linwood, Me. 01623
800-615-2284
508-762-2284
Fax: 508-762-2231
Cell: Person Cell number
email address

Logo Text

Large enough to service small enough to care

Font styles to use
Serif

Colors
0355a3

Requirements
Must have
• Commercial and Residential Roofing contractor needs design logo and card design. Can be single or double sided but must incorporate:
• Persons Name:
• Persons Title:
• Mailing Address: PO Box 3716
• Physical Address: 41 Birch Lane
• Linwood, Me. 01623
• 800-615-2284
• 508-762-2284
• Fax: 508-762-2231
• Cell: Person Cell number
• email address
• Website: WWW.harborcrestexteriors.example
Nice to have
• ..
Should not have
• I'm looking for something different. I have had the same card for 23 years. I attached what both sides of my present card looks like.

```html
<!DOCTYPE html>
<html lang="en">
<head>
<meta charset="utf-8">
<title>Harbor Crest Exteriors Inc – Business Card</title>
<link rel="stylesheet" href="https://fonts.googleapis.com/css2?family=Didact+Gothic&family=Mulish:ital,wght@0,700;1,300;1,400&display=swap">
<style>
  :root {
    --backdrop: #1b1b1b;
    --paper: #ffffff;
    --brand-blue: #1a3690;
    --brand-navy: #032b61;
    --accent-grey: #d2d1d4;
    --ink: #333333;
    --on-blue: #ffffff;
    --on-blue-soft: #e6e9f5;
  }
  * { margin: 0; padding: 0; box-sizing: border-box; }
  html, body {
    width: 1200px; height: 910px; overflow: hidden;
    background: var(--backdrop);
  }
  .business-card {
    position: absolute;
    left: 253px; top: 255px;
    width: 696px; height: 398px;
    background: var(--paper);
    overflow: hidden;
  }
  .chevron-panel {
    position: absolute; inset: 0;
    width: 100%; height: 100%;
  }
  .brand {
    position: absolute;
    left: 48px; top: 62px;
    width: 240px;
    text-align: center;
  }
  .brand-mark {
    display: block;
    width: 54px; height: 54px;
    margin: 0 auto 14px;
    background: var(--brand-blue);
  }
  .brand-name {
    font-family: "Didact Gothic", sans-serif;
    font-size: 21px;
    letter-spacing: 1.5px;
    color: var(--brand-blue);
    white-space: nowrap;
  }
  .company-contact {
    position: absolute;
    left: 63px; top: 255px;
    font-family: "Didact Gothic", sans-serif;
    font-size: 18.5px;
    line-height: 22.3px;
    color: var(--ink);
    list-style: none;
  }
  .company-contact li { white-space: nowrap; }
  .person {
    position: absolute;
    right: 66px; top: 177px;
    text-align: right;
    font-family: "Mulish", sans-serif;
    color: var(--on-blue);
  }
  .person-name { font-weight: 700; font-size: 24px; line-height: 30px; }
  .person-title { font-weight: 400; font-style: italic; font-size: 24px; line-height: 30px; }
  .phone-list {
    position: absolute;
    top: 263px; left: 0;
    list-style: none;
    font-family: "Mulish", sans-serif;
    font-style: italic; font-weight: 300;
    font-size: 18.5px; line-height: 26.2px;
    color: var(--on-blue-soft);
  }
  .phone-list li { position: relative; white-space: nowrap; }
  .phone-list .line-1 { left: 426px; }
  .phone-list .line-2 { left: 436px; }
  .phone-list .line-3 { left: 447px; }
  .phone-list .line-4 { left: 457px; }
</style>
</head>
<body>
  <section class="business-card">
    <svg class="chevron-panel" viewBox="0 0 718 411" preserveAspectRatio="none" aria-hidden="true">
      <polygon fill="var(--accent-grey)" points="412,0 718,0 718,411 412,411 312,205"/>
      <polygon fill="var(--brand-navy)" points="436,0 718,0 718,411 436,411 336,205"/>
      <polygon fill="var(--brand-blue)" points="451,0 718,0 718,411 451,411 351,205"/>
    </svg>

    <div class="brand">
      <span class="brand-mark"></span>
      <div class="brand-name">harbor crest exteriors</div>
    </div>

    <ul class="company-contact">
      <li>41 Birch Lane</li>
      <li>PO Box 3716</li>
      <li>Linwood, Me. 01623</li>
      <li>dana@harborcrest.example</li>
      <li>www.harborcrestexteriors.example</li>
    </ul>

    <div class="person">
      <div class="person-name">Dana Whitfield</div>
      <div class="person-title">president</div>
    </div>

    <ul class="phone-list">
      <li class="line-1">800.615.2284</li>
      <li class="line-2">508.762.2284</li>
      <li class="line-3">fax: 508.762.2231</li>
      <li class="line-4">cell: 508.555.0148</li>
    </ul>
  </section>
</body>
</html>
```